Saveurs Du Matin

looking fo an e-commerce site something that will stand out the site domain will be saveursdumatin.example need somthing bold and refind as well; eye appealing and not too cartonish please visit our competetors to see waht we are going for they are (tastrovel.example, brenza4u.example and calvanopresses.example) this site should have multiple pages mainly looking for a layout to start the site and code.

PLEASE REMEMBER WE REQUIRE THE CODE....

Target Market(s)

anyone who loves food or is fasinated by it

Industry/Entity Type

E-Commerce

Requirements
Must have
• .an easy to work site that makes sense and that is not all over the place it should have in the navigation feature: Olive oils, Balsamic Vinegars, Misc. Vinegars and oils, Specialty salts, organic spices, Specialty Spices, Kitchen Tools. also pleas use our logo in the design i have attached below
Nice to have
• clean and some spices, salt, pepermills, morter and pistels, olive oils, trying to stick to a clean presentation
Should not have
• no cartoon figures or alike, anything too playfull

```html
<!DOCTYPE html>
<html lang="en">
<head>
<meta charset="utf-8">
<title>Saveurs Du Matin — Highest Quality Spices</title>
<link rel="stylesheet" href="https://fonts.googleapis.com/css2?family=Cabin:wght@400;500&family=Cinzel:wght@400;700&display=swap">
<style>
  :root {
    --sand-outer: #e9a883;
    --sand-outer-light: #f2c2a0;
    --page: #fcd9a4;
    --page-light: #fde3b8;
    --ink: #4a2a0c;
    --brown: #5b3817;
    --rust: #a33d16;
    --accent: #c9693c;
    --line: #6b3a16;
    --green: #7bb31d;
    --green-dark: #4f7c06;
    --panel: #f4cf9c;
    --panel-border: #d8ae78;
    --underline: #e8584a;
  }
  * { box-sizing: border-box; margin: 0; padding: 0; }
  html, body { width: 1200px; height: 900px; overflow: hidden; }
  body {
    position: relative;
    font-family: "Cabin", sans-serif;
    color: var(--ink);
    background: linear-gradient(160deg, var(--sand-outer-light), var(--sand-outer) 55%, #e39d78);
  }
  .clove-decoration {
    position: absolute; left: 1104px; top: 28px; width: 96px; height: 250px;
    background: linear-gradient(180deg, #5a2e14, #3a1c0b);
    opacity: .55; border-radius: 40px;
  }
  .page {
    position: absolute; left: 100px; top: 0; width: 1000px; height: 900px;
    background: linear-gradient(175deg, var(--page-light), var(--page) 60%, #f9cf92);
  }
  .abs { position: absolute; }

  .top-links { left: 31px; top: 34px; display: flex; gap: 45px; font-size: 19px; letter-spacing: 2px; color: var(--brown); }
  .search {
    left: 29px; top: 77px; width: 145px; height: 35px;
    border: 1px dotted var(--brown); border-radius: 6px;
    display: flex; align-items: center; gap: 12px; padding-left: 10px;
    font-size: 14px; letter-spacing: 2px; color: #b59670;
  }
  .brand {
    left: 405px; top: 14px; width: 170px; height: 131px;
    background: #fff; border: 1px solid #b06a3a;
    display: flex; flex-direction: column; align-items: center; justify-content: center; gap: 10px;
  }
  .brand-dot { width: 44px; height: 44px; border-radius: 50%; background: #8a4a23; }
  .brand-name { font-size: 16px; color: #8a4a23; }

  .cart-bag {
    left: 705px; top: 35px; width: 82px; height: 90px; border-radius: 6px;
    background: linear-gradient(135deg, #a6d83a, var(--green) 55%, var(--green-dark));
  }
  .start-shopping { left: 797px; top: 36px; font-size: 34px; line-height: 42px; letter-spacing: 1px; color: var(--accent); }

  .rule { left: 0; width: 1000px; border-top: 1px solid var(--line); }
  .main-nav {
    left: 0; top: 147px; width: 1000px; display: flex; justify-content: space-between;
    padding: 0 15px 0 10px; font-size: 14.5px; color: var(--ink);
  }

  .hero {
    left: 0; top: 183px; width: 1001px; height: 319px;
    background: linear-gradient(100deg, #b9b3ae 0%, #8e8a86 35%, #6b6661 60%, #a59f98 85%, #c8bfb4 100%);
  }
  .hero-title {
    font-family: "Cinzel", serif; font-size: 54px; letter-spacing: 3px;
    color: #eee9e4; text-shadow: 2px 2px 0 #777, 0 0 6px rgba(0,0,0,.3);
  }
  .hero-next {
    left: 968px; top: 334px; width: 58px; height: 58px; border-radius: 50%;
    background: rgba(240,232,222,.85); display: flex; align-items: center; justify-content: center;
  }

  .tile { top: 536px; height: 211px; }
  .tile-sweet {
    left: -1px; width: 267px; border: 3px solid #b1b38c;
    background: linear-gradient(160deg, #f2ede6, #e3cdb4 45%, #b57a52 70%, #efe6db);
  }
  .tile-meat {
    left: 366px; width: 266px; border: 1px dotted #8a6a3a;
    background: linear-gradient(150deg, #e8b43a, #d2961f 50%, #b7791a);
  }
  .tile-label { font-family: "Cinzel", serif; font-size: 42px; line-height: 42px; }
  .tile-sweet .tile-label { left: 30px; top: 80px; color: #6b3a26; text-shadow: 1px 1px 0 #f4e5d6; }
  .tile-meat .tile-label { left: 34px; top: 52px; text-align: center; color: rgba(255,240,225,.75); font-size: 46px; }

  .social-panel {
    left: 734px; top: 536px; width: 266px; height: 210px;
    background: var(--panel); border: 1px solid var(--panel-border);
  }
  .social-intro { left: 9px; top: 11px; font-size: 15px; letter-spacing: 1px; }
  .social-dot {
    top: 42px; width: 44px; height: 44px; border-radius: 50%;
    background: radial-gradient(circle at 40% 35%, #fff, #e6e6e6 60%, #c9c9c9);
    box-shadow: 0 2px 4px rgba(0,0,0,.25);
  }
  .newsletter-note { left: 16px; top: 100px; width: 240px; font-size: 15px; line-height: 21px; letter-spacing: 1px; }
  .ask-underline { left: 68px; top: 146px; width: 111px; border-top: 3px solid var(--underline); }
  .newsletter-button {
    left: 28px; top: 160px; width: 202px; height: 40px; border-radius: 8px;
    background: linear-gradient(180deg, #9ed13a, var(--green) 50%, var(--green-dark));
    border: 1px solid #3a5a06; box-shadow: 2px 3px 4px rgba(0,0,0,.3);
    font-family: "Cinzel", serif; font-weight: 700; font-size: 15px; letter-spacing: 3px;
    color: #4a2a0c; display: flex; align-items: center; justify-content: center;
  }

  .policy-links { left: 10px; top: 790px; display: flex; flex-direction: column; gap: 9px; font-size: 19px; color: var(--rust); }
  .footer-links { top: 790px; font-size: 19px; color: var(--ink); }
  .footer-email { left: 538px; top: 870px; font-size: 14px; color: #111; }
</style>
</head>
<body>
  <div class="clove-decoration" role="img" aria-label="Whole cloves scattered at the page edge"></div>

  <div class="page">
    <nav class="abs top-links"><span>CONTACT</span><span>BLOG</span></nav>
    <div class="abs search">
      <svg width="28" height="24" viewBox="0 0 28 24"><circle cx="17" cy="9" r="7" fill="none" stroke="#3a2a1a" stroke-width="2"/><line x1="12" y1="14" x2="3" y2="22" stroke="#3a2a1a" stroke-width="3" stroke-linecap="round"/></svg>
      <span>Search</span>
    </div>

    <div class="abs brand">
      <span class="brand-dot"></span>
      <span class="brand-name">Saveurs Du Matin</span>
    </div>

    <div class="abs cart-bag" role="img" aria-label="Green shopping bag"></div>
    <div class="abs start-shopping">START<br>SHOPPING</div>

    <div class="abs rule" style="top:131px"></div>
    <div class="abs rule" style="top:135px"></div>
    <nav class="abs main-nav">
      <span>OLIVE OILS</span><span>BALSAMIC VINEGARS</span><span>VINEGARS AND OILS</span><span>SPECIALITY SALTS</span><span>ORGANIC SPICES</span><span>SPECIALITY SPICES</span><span>KITCHEN TOOLS</span>
    </nav>
    <div class="abs rule" style="top:181px"></div>

    <section class="abs hero" role="img" aria-label="Table spread with avocado, salt, cheese, relish and fresh salsa"></section>
    <div class="abs hero-title" style="left:155px;top:218px">FRUITS OF THE</div>
    <div class="abs hero-title" style="left:140px;top:362px">EARTH</div>
    <div class="abs hero-next">
      <svg width="26" height="20" viewBox="0 0 26 20"><path d="M2 7h12V2l10 8-10 8v-5H2z" fill="#8a7a4a"/></svg>
    </div>

    <div class="abs tile tile-sweet" role="img" aria-label="Cinnamon sticks">
      <span class="abs tile-label">SWEET</span>
    </div>
    <div class="abs tile tile-meat" role="img" aria-label="Pile of whole nutmegs">
      <span class="abs tile-label">FOR<br>MEAT</span>
    </div>

    <aside class="abs social-panel">
      <p class="abs social-intro">If you like us we are also here</p>
      <span class="abs social-dot" style="left:29px"></span>
      <span class="abs social-dot" style="left:102px"></span>
      <span class="abs social-dot" style="left:180px"></span>
      <p class="abs newsletter-note">For special sales, events and more, ASK for our</p>
      <span class="abs ask-underline"></span>
      <div class="abs newsletter-button">NEWSLETTER</div>
    </aside>

    <div class="abs rule" style="top:781px"></div>
    <div class="abs rule" style="top:785px"></div>
    <nav class="abs policy-links"><span>Shopping policy</span><span>Privacy policy</span><span>Terms of service</span></nav>
    <span class="abs footer-links" style="left:368px">ABOUT US</span>
    <span class="abs footer-links" style="left:538px">CONTACT</span>
    <span class="abs footer-email">hello@saveursdumatin.example</span>
  </div>
</body>
</html>
```